Commercial photographer, UAV drone photography & 360 walk-through visuals

I need a business card design that is minimalist but yet pretentiously creative. My target market are architects, designers, advertising agents and marketing managers. It is important to stress that though I am asking for a minimalist design it needs to have creative impact.

Target Market(s)

Architects, interiors designers, web-designers, artists

Contact Information for Business Card

Include my name, mobile [cell] number, email, web page and the company logo. Do not to include a postal address.

Colors

Designer to choose colors to be used in the design.

Requirements
Must have
• The following information is to be included:
• Milo Fenwick
• Photographer
• m: 07812 593174
• e: milo@mfimagery.co.uk
• w: mfimagery.co.uk

```html
<!DOCTYPE html>
<html lang="en">
<head>
<meta charset="utf-8">
<title>MF Imagery – Business Card</title>
<link href="https://fonts.googleapis.com/css2?family=Montserrat:wght@600&family=Questrial&display=swap" rel="stylesheet">
<style>
  :root {
    --stage: #4a4f51;
    --card-light: #ffffff;
    --card-dark: #000000;
    --ink-dark: #1d1b1c;
    --ink-light: #ffffff;
  }
  html, body {
    margin: 0;
    padding: 0;
    overflow: hidden;
  }
  .canvas {
    position: relative;
    width: 1200px;
    height: 1000px;
    background: var(--stage);
    overflow: hidden;
  }
  .card {
    position: absolute;
    width: 715px;
    height: 409px;
    box-shadow: 0 6px 18px rgba(0,0,0,0.45);
  }
  .card--front {
    left: 120px;
    top: 75px;
    background: var(--card-light);
  }
  .card--back {
    left: 380px;
    top: 521px;
    background: var(--card-dark);
  }
  .brand {
    position: absolute;
    display: flex;
    align-items: center;
    gap: 14px;
    font-family: "Questrial", sans-serif;
    letter-spacing: 0.06em;
    white-space: nowrap;
  }
  .brand__dot {
    border-radius: 50%;
    flex: none;
  }
  .card--front .brand {
    left: 50%;
    top: 50%;
    transform: translate(-50%, -50%);
    font-size: 40px;
    color: var(--ink-dark);
  }
  .card--front .brand__dot {
    width: 22px;
    height: 22px;
    background: var(--ink-dark);
  }
  .card--back .brand {
    left: 88px;
    top: 158px;
    font-size: 28px;
    color: var(--ink-light);
    gap: 10px;
  }
  .card--back .brand__dot {
    width: 15px;
    height: 15px;
    background: var(--ink-light);
  }
  .holder-name {
    position: absolute;
    left: 383px;
    top: 60px;
    margin: 0;
    font-family: "Montserrat", sans-serif;
    font-weight: 600;
    font-size: 18px;
    letter-spacing: 0.32em;
    text-transform: uppercase;
    color: var(--ink-light);
  }
  .contact-list {
    position: absolute;
    left: 378px;
    top: 228px;
    margin: 0;
    padding: 0;
    list-style: none;
    font-family: "Questrial", sans-serif;
    font-size: 23px;
    color: var(--ink-light);
  }
  .contact-list__item {
    display: flex;
    align-items: center;
    gap: 10px;
    height: 26px;
    margin-bottom: 12px;
  }
  .contact-list__icon {
    width: 22px;
    height: 22px;
    flex: none;
    fill: var(--ink-light);
    stroke: var(--ink-light);
  }
</style>
</head>
<body>
<main class="canvas">

  <section class="card card--front" aria-label="Business card front">
    <div class="brand">
      <span class="brand__dot"></span>
      <span class="brand__name">MF IMAGERY</span>
    </div>
  </section>

  <section class="card card--back" aria-label="Business card back">
    <div class="brand">
      <span class="brand__dot"></span>
      <span class="brand__name">MF IMAGERY</span>
    </div>

    <h1 class="holder-name">Milo Fenwick</h1>

    <ul class="contact-list">
      <li class="contact-list__item">
        <svg class="contact-list__icon" viewBox="0 0 24 24" aria-hidden="true">
          <path stroke="none" d="M6.6 2.5c.6-.3 1.3-.1 1.6.5l2 3.6c.3.6.2 1.2-.3 1.6L8.4 9.4c.9 2.2 3.5 4.9 5.9 5.9l1.3-1.5c.4-.5 1.1-.6 1.6-.3l3.6 2c.6.3.8 1 .5 1.6l-1.1 2.2c-.5 1-1.6 1.6-2.7 1.3C10.3 19 5.1 13.8 3.4 6.7c-.3-1.1.3-2.2 1.3-2.7z"/>
        </svg>
        <span>07812 593174</span>
      </li>
      <li class="contact-list__item">
        <svg class="contact-list__icon" viewBox="0 0 24 24" aria-hidden="true">
          <rect x="2" y="5" width="20" height="14" stroke="none"/>
          <path d="M2.5 5.5 12 13l9.5-7.5" fill="none" stroke="#000" stroke-width="1.6"/>
        </svg>
        <span>milo@mfimagery.co.uk</span>
      </li>
      <li class="contact-list__item">
        <svg class="contact-list__icon" viewBox="0 0 24 24" aria-hidden="true" fill="none" stroke-width="1.8">
          <circle cx="12" cy="12" r="9.5" fill="none"/>
          <ellipse cx="12" cy="12" rx="4.2" ry="9.5" fill="none"/>
          <path d="M2.5 12h19M4 7h16M4 17h16" fill="none"/>
        </svg>
        <span>www.mfimagery.co.uk</span>
      </li>
    </ul>
  </section>

</main>
</body>
</html>
```